Moderner, schlichter Flyer in Corporate Design
Zielgruppe
Auszubildene, Absolventen, Arbeitssuchende: BewerberInnen aller Altersklassen.
Aufgabenstellung
Liebe DesignerIn,
klarKarriere ist ein Onlinedienstleister, der im Kundenauftrag Bewerbungsunterlagen optimiert oder komplett erstellt. Für eine Kampagne suchen wir nun nach einem Design für neue Flyer.
Bei überzeugendem Ergebnis würden wir uns freuen Ihre Dienste auch zukünftig in Anspruch zu nehmen. Wir haben uns bemüht spezifische Angaben im Briefing zu erstellen, sollten Sie zusätzliche Rückfragen haben, beantworten wir diese innerhalb der Kommentare gerne. Bitte beachten Sie unbedingt unsere Vorgaben!
Wir wünschen allen Teilnehmern viel Erfolg und freuen uns auf ansprechende Entwürfe!

```html
<!DOCTYPE html>
<html lang="de">
<head>
<meta charset="utf-8">
<title>klarKarriere Flyer</title>
<link href="https://fonts.googleapis.com/css2?family=Open+Sans:wght@400;600;700;800&family=Cousine&display=swap" rel="stylesheet">
<style>
:root{
  --blue:#2d5a8b;
  --orange:#d2611f;
  --orange-light:#f29a2c;
  --green:#7cc04a;
  --green-light:#a6dc6e;
  --grey:#cacbcd;
  --ink:#1d1d1d;
  --white:#ffffff;
  --page:#ffffff;
}
*{box-sizing:border-box;margin:0;padding:0}
html,body{width:1200px;height:1101px;overflow:hidden;background:var(--page);font-family:"Open Sans",Arial,sans-serif}
.stage{position:relative;width:1200px;height:1101px}
.flyer{position:absolute;top:170px;width:540px;height:760px;overflow:hidden;box-shadow:0 4px 18px rgba(0,0,0,.18)}
.flyer--front{left:40px;background:var(--blue)}
.flyer--back{left:620px;background:var(--orange)}
.burst{position:absolute;display:flex;flex-direction:column;align-items:center;justify-content:center;text-align:center;
  clip-path:polygon(100% 50%,93.2% 58.6%,96.2% 69.1%,86.6% 74.5%,85.4% 85.4%,74.5% 86.6%,69.1% 96.2%,58.6% 93.2%,50% 100%,41.4% 93.2%,30.9% 96.2%,25.5% 86.6%,14.6% 85.4%,13.4% 74.5%,3.8% 69.1%,6.8% 58.6%,0 50%,6.8% 41.4%,3.8% 30.9%,13.4% 25.5%,14.6% 14.6%,25.5% 13.4%,30.9% 3.8%,41.4% 6.8%,50% 0,58.6% 6.8%,69.1% 3.8%,74.5% 13.4%,85.4% 14.6%,86.6% 25.5%,96.2% 30.9%,93.2% 41.4%)}
.burst--price{top:26px;right:26px;width:150px;height:150px;background:radial-gradient(circle,var(--orange-light),var(--orange));color:var(--white);font-weight:700;line-height:1.05}
.burst--price .big{font-size:30px}
.burst--price .small{font-size:18px}
.burst--sale{width:96px;height:96px;background:radial-gradient(circle,var(--green-light),var(--green));color:var(--white);font-weight:700;font-size:15px;line-height:1.05}
.flyer--front .burst--sale{left:34px;top:530px}
.flyer--back .burst--sale{left:22px;top:34px}
.figure{position:absolute;background:linear-gradient(180deg,#c9ccd1,#9ea4ad);border-radius:40px}
.flyer--front .figure{left:36px;top:160px;width:115px;height:170px;opacity:.85}
.brand{position:absolute;font-weight:700;letter-spacing:-1px;line-height:1}
.flyer--front .brand{left:165px;top:215px;font-size:54px;color:var(--white)}
.headline{position:absolute;left:60px;top:342px;font-size:28px;font-weight:700;color:var(--orange)}
.offers{position:absolute;left:60px;top:392px;width:440px;list-style:none;color:var(--white);font-size:16px;font-weight:600;line-height:1.35}
.offers li{position:relative;padding-left:28px;margin-bottom:12px}
.offers li::before{content:"";position:absolute;left:0;top:5px;width:14px;height:14px;border-radius:50%;background:radial-gradient(circle at 35% 35%,var(--orange-light),var(--orange))}
.offers .indent{display:block;margin-top:4px}
.promo-note{position:absolute;left:150px;top:540px;width:360px;color:var(--white);font-size:15.5px;font-weight:600;line-height:1.35}
.front-footer{position:absolute;left:0;bottom:0;width:100%;height:100px;background:var(--orange);display:flex;align-items:center;justify-content:center;color:var(--white);font-size:30px;font-weight:600}
.back-title{position:absolute;left:140px;top:40px;width:380px;color:var(--white);font-size:31px;font-weight:700;line-height:1.2}
.steps{position:absolute;left:40px;top:190px;width:470px;color:var(--ink);font-size:17px;font-weight:600;line-height:1.3}
.steps strong{display:block;font-size:15px;font-weight:800;margin-bottom:6px}
.fineprint{position:absolute;left:40px;top:330px;width:200px;color:var(--white);font-size:9.5px;line-height:1.35}
.burst--code{left:270px;top:300px;width:220px;height:220px;background:var(--white);font-family:"Cousine",monospace;font-size:34px;color:var(--ink);line-height:1.3}
.more{position:absolute;left:150px;top:548px;color:var(--white);font-size:18px;font-weight:700}
.flyer--back .figure{left:40px;top:570px;width:100px;height:120px}
.flyer--back .brand{left:160px;top:600px;font-size:50px;color:var(--blue)}
.back-footer{position:absolute;left:0;bottom:0;width:100%;height:90px;background:var(--grey)}
.back-footer .url{position:absolute;left:160px;top:14px;color:var(--blue);font-size:19px;font-weight:700}
.back-footer .legal{position:absolute;left:0;right:0;bottom:12px;text-align:center;font-size:9px;color:var(--ink)}
</style>
</head>
<body>
<main class="stage">
  <section class="flyer flyer--front">
    <div class="burst burst--price"><span class="small">ab</span><span class="big">29,90 €</span><span class="small">monatlich</span></div>
    <div class="figure" role="img" aria-label="Illustration einer jubelnden Person mit Bewerbungsmappe"></div>
    <div class="brand">klarKarriere</div>
    <h2 class="headline">Wie bieten Ihnen:</h2>
    <ul class="offers">
      <li>Professionelle &amp; individuelle Bewerbungsunterlagen per Mausklick <span class="indent">ab 29,90 € im Monat.</span></li>
      <li>Lassen Sie Ihre Bewerbungsunterlagen von Experten erstellen oder optimieren</li>
    </ul>
    <div class="burst burst--sale">5 %<br>Rabatt<br>Aktion</div>
    <p class="promo-note">Auf unseren Service erhalten Sie einmalig 5% Rabatt bei Eingabe des rückseitigen Aktions-Codes im Internet.</p>
    <div class="front-footer">www.klarKarriere.de</div>
  </section>

  <section class="flyer flyer--back">
    <div class="burst burst--sale">5 %<br>Rabatt<br>Aktion</div>
    <h2 class="back-title">Holen Sie Ihren Erfolg per Mausklick und sparen Sie 5% !</h2>
    <p class="steps"><strong>Und so einfach geht's:</strong>Tragen Sie auf unserer Internetseite www.klarKarriere.de folgenden Aktions-Code* in das dafür vorgesehene Feld:</p>
    <p class="fineprint">*Der Aktions-Code kann einmalig eingelöst und nicht übertragen werden. Eine Auszahlung des Gegenwertes in bar sowie die Kombination mit anderen Aktionen ist nicht möglich. klarKarriere behält sich vor, einzelne Produkte von der Aktion auszuschließen</p>
    <div class="burst burst--code">12345-<br>ABCDE</div>
    <p class="more">Mehr Informationen finden Sie auf:</p>
    <div class="figure" role="img" aria-label="Illustration einer jubelnden Person mit Bewerbungsmappe"></div>
    <div class="brand">klarKarriere</div>
    <div class="back-footer">
      <span class="url">www.klarKarriere.de</span>
      <span class="legal">© klarKarriere UG (haftungsbeschränkt) / info@klarKarriere.de</span>
    </div>
  </section>
</main>
</body>
</html>
```